Vantrisco website redesign

1.logo redesign
2. whole website lay out redesign
3. add more function and pages (have some detail in attachment).
4. design the info taking form layout(contact us, return request, trade pro, see all form in file)
5. also design the mobile look for the website
some reference website: https://www.plaquevora.example/
https://www.moskuden.example/

we want our website style between these two website, website should be user friendly focus + slight design style, and mobile one could more like https://www.moskuden.example/ (more design style)

Target Market(s)

Tile Ecommerce

Industry/Entity Type

Ecommerce, Tile

Coding

Coded - Design and coding required

Number of Pages Required

5+ page

```html
<!DOCTYPE html>
<html lang="en">
<head>
<meta charset="utf-8">
<title>Vantrisco – Edit Account Information</title>
<link href="https://fonts.googleapis.com/css2?family=Figtree:wght@400;500;600;700&display=swap" rel="stylesheet">
<style>
:root{
  --ink:#40444d;
  --ink-soft:#5a5e66;
  --muted:#b4b6ba;
  --line:#ececec;
  --bar:#40444d;
  --header:#f5f5f5;
  --nav:#efefef;
  --side:#f2f2f2;
  --btn:#d4d4d4;
  --accent:#e53935;
  --white:#fff;
  --foot-text:#a7a9ad;
}
*{box-sizing:border-box;margin:0;padding:0}
html,body{width:1200px;height:998px;overflow:hidden;background:var(--white);font-family:"Figtree",sans-serif;color:var(--ink)}
.page{position:relative;width:1200px;height:998px}
.abs{position:absolute}
.topbar{left:0;top:0;width:1200px;height:31px;background:var(--bar);color:var(--white);font-size:9.5px;display:flex;align-items:center;justify-content:center}
.social{position:absolute;display:flex;gap:11px}
.social span{width:11px;height:11px;border:1.2px solid #9fa2a8;border-radius:50%}
.header{left:0;top:31px;width:1200px;height:46px;background:var(--header)}
.brand{font-weight:700;color:var(--ink);letter-spacing:.2px}
.search{left:745px;top:16px;display:flex;align-items:center;gap:10px;font-size:11px;color:#8a8d92}
.icons{left:962px;top:14px;display:flex;gap:12px;align-items:center}
.cart-count{left:1035px;top:10px;font-size:8px;font-weight:600}
.nav{left:0;top:77px;width:1200px;height:34px;background:var(--nav);font-size:10.6px;color:var(--ink-soft)}
.nav a{position:absolute;top:11px;text-decoration:none;color:inherit}
.side-title{left:156px;top:139px;font-size:13px;font-weight:600}
.side-menu{left:156px;top:171px;width:169px;list-style:none}
.side-menu li{height:31px;margin-bottom:1px;background:var(--side);font-size:10.8px;padding-left:13px;line-height:31px}
.side-menu li.active{background:var(--ink);color:var(--white)}
.main{left:369px;top:137px;width:598px}
.main h1{font-size:19px;font-weight:600;margin-bottom:23px}
.section{font-size:12px;font-weight:600;padding-bottom:9px;border-bottom:1px solid var(--line)}
.field{margin-top:14px}
.field label{display:block;font-size:10.6px;margin-bottom:5px}
.req{color:var(--accent)}
.field .input{width:288px;height:32px;border:1px solid #d6d6d6;border-radius:2px;font-size:10.5px;color:var(--muted);padding-left:13px;line-height:30px}
.checks{margin-top:20px;font-size:10.8px}
.checks div{display:flex;align-items:center;gap:6px;height:13px;margin-bottom:8px}
.box{width:13px;height:13px;border:1px solid #cfcfcf;border-radius:2px}
.actions{left:369px;top:570px;width:598px;height:52px;border-top:1px solid var(--line)}
.back{left:0;top:25px;font-size:11px;color:#9a9da2;text-decoration:underline}
.save{left:57px;top:19px;width:125px;height:32px;background:var(--btn);border-radius:3px;font-size:12px;font-weight:500;display:flex;align-items:center;justify-content:center}
.required{right:0;top:25px;font-size:9.5px;color:var(--accent)}
.footer{left:0;top:765px;width:1200px;height:199px;background:linear-gradient(135deg,#2a2d33,#34373d 55%,#2b2e34)}
.foot-logo{left:156px;top:45px;font-size:31px;color:var(--white)}
.col{top:48px;color:var(--foot-text);font-size:11px}
.col h3{color:var(--white);font-size:13.5px;font-weight:600;margin-bottom:12px}
.col p{height:19px}
.contact p{display:flex;gap:6px;height:24px}
.chat{left:1006px;top:130px}
.bottom{left:0;top:964px;width:1200px;height:34px;background:var(--bar);color:var(--white);font-size:11px}
</style>
</head>
<body>
<div class="page">
  <div class="abs topbar">Wholesale, Over 150 Square Feet. 10% Off
    <div class="social" style="left:985px;top:10px"><span></span><span></span><span></span></div>
  </div>

  <div class="abs header">
    <div class="abs brand" style="left:156px;top:8px;font-size:25px">Vantrisco</div>
    <div class="abs search">
      <svg width="14" height="14" viewBox="0 0 14 14" fill="none" stroke="#40444d" stroke-width="1.2"><circle cx="8" cy="6" r="4.6"/><path d="M4.6 9.4 1 13"/></svg>
      search here
    </div>
    <div class="abs icons">
      <svg width="14" height="15" viewBox="0 0 14 15" fill="none" stroke="#40444d" stroke-width="1.2"><circle cx="7" cy="4.5" r="3.3"/><path d="M1 14.5c0-3.5 2.7-5.5 6-5.5s6 2 6 5.5"/></svg>
      <svg width="16" height="14" viewBox="0 0 16 14" fill="none" stroke="#40444d" stroke-width="1.2"><path d="M8 13 1.8 6.9A3.6 3.6 0 0 1 8 2.3a3.6 3.6 0 0 1 6.2 4.6Z"/></svg>
      <svg width="14" height="15" viewBox="0 0 14 15" fill="none" stroke="#40444d" stroke-width="1.2"><path d="M1 4.5h12v10H1z"/><path d="M4.3 4.5V3a2.7 2.7 0 0 1 5.4 0v1.5"/></svg>
    </div>
    <div class="abs cart-count">0</div>
  </div>

  <nav class="abs nav">
    <a style="left:156px">Ceramic</a><a style="left:234px">Porcelain</a><a style="left:318px">Glass</a><a style="left:381px">Marble</a><a style="left:453px">Fixtures</a>
    <a style="left:853px">Showrooms</a><a style="left:940px">Trade</a><a style="left:996px">About Us</a>
  </nav>

  <div class="abs side-title">My Account</div>
  <ul class="abs side-menu">
    <li>Account Dashboard</li>
    <li class="active">Account Information</li>
    <li>Address Book</li>
    <li>My Orders</li>
    <li>My Credit Cards</li>
  </ul>

  <main class="abs main">
    <h1>Edit Account Information</h1>
    <div class="section">Account Information</div>
    <div class="field"><label>First Name<span class="req">*</span></label><div class="input">type here</div></div>
    <div class="field"><label>Middle Name / Initial</label><div class="input">type here</div></div>
    <div class="field"><label>Last Name<span class="req">*</span></label><div class="input">type here</div></div>
    <div class="checks">
      <div><span class="box"></span>Change Email</div>
      <div><span class="box"></span>Change Password</div>
    </div>
    <div class="section" style="margin-top:25px">Additional Information</div>
  </main>

  <div class="abs actions">
    <div class="abs back">Back</div>
    <div class="abs save">Save</div>
    <div class="abs required">*Required Fields</div>
  </div>

  <footer class="abs footer" role="img" aria-label="Dark stone tile texture background">
    <div class="abs brand foot-logo">Vantrisco</div>
    <div class="abs col contact" style="left:407px">
      <h3>Contact Us</h3>
      <p><svg width="10" height="10" viewBox="0 0 10 10" fill="#fff"><path d="M2 0.5 3.8 2.6 2.8 3.8a6 6 0 0 0 3.4 3.4l1.2-1 2.1 1.8-1 1.5C4.5 9.5.5 5.5.5 1.5Z"/></svg><b style="font-weight:600">555-014-2736</b></p>
      <p><svg width="10" height="10" viewBox="0 0 10 10" fill="#fff"><path d="M0 3.5 5 0.5l5 3V9.5H0Z"/></svg>info@vantrisco.example</p>
      <p style="height:auto"><svg width="11" height="11" viewBox="0 0 11 11"><circle cx="5.5" cy="5.5" r="5.5" fill="#fff"/><path d="M5.5 2.5v3h2" stroke="#30333a" fill="none"/></svg><span style="line-height:17px">Monday to Friday,<br>9:00 AM - 4:00PM EST</span></p>
    </div>
    <div class="abs col" style="left:612px">
      <h3>Client Experience</h3>
      <p>Shipping &amp; Returns</p><p>FAQs</p><p>Track My Order</p><p>Installation</p>
    </div>
    <div class="abs col" style="left:818px">
      <h3>Quick Links</h3>
      <p>About Us</p><p>Inspiration</p><p>Trade</p><p>Join The Team</p>
    </div>
    <svg class="abs chat" width="38" height="38" viewBox="0 0 38 38"><path d="M19 1a18 18 0 1 1-8 34.2L2 37l2.5-8A18 18 0 0 1 19 1Z" fill="#fff"/><path d="M11 16h12M11 21h17" stroke="#2f3238" stroke-width="2.6" stroke-linecap="round"/></svg>
  </footer>

  <div class="abs bottom">
    <div class="abs" style="left:156px;top:10px">© 2024 Vantrisco. All Right Reserved</div>
    <div class="social" style="left:984px;top:11px"><span></span><span></span><span></span></div>
  </div>
</div>
</body>
</html>
```